Corporate marketing website with signup form

The function of the website is to promote our 2 product offerings. It will contain a main screen and several 5-7 sub-pages that will be available as 'scroll down' anchors and as front-page navigation links on the top of the page.

Navigation menu labels are: Products, Unique Model, Pricing, About, and Contact

Target Market(s)

Business to business marketers who are looking to source lead generation services

Industry/Entity Type

Marketing

Logo Text

Velmora

Coding

Coded - Design and coding required

Number of Pages Required

5+ page

Requirements
Must have
• A sign-up form on main section of the front page. Fields are First Name, Last Name, Company, and Email (all text), and a pull-down with three options (only pick one): Track 1, Track 2, Custom Combination.
• Also incorporate the bottom half (ie crop the image) of the EPS file attached (the 'blue heads). Add this to the lower portion of the main screen and have the rest of the blue background become the background for the next anchored section of the navigation.
• You'll see the main section text in the mock-up I provided. The rest of the menu items/anchors can be lorem ipsum for now.
• Can this be coded in Wordpress? That would be my preference so I can edit it in the future.

```html
<!DOCTYPE html>
<html lang="en">
<head>
<meta charset="utf-8">
<title>Velmora — Lead Generation</title>
<link rel="stylesheet" href="https://fonts.googleapis.com/css2?family=Roboto:wght@300;400;500&family=Roboto+Condensed:wght@400;700&display=swap">
<style>
:root{
  --hero-top:#4f8cbf;
  --hero:#6aa4d2;
  --hero-light:#7db3dd;
  --card-head:#2d6a9b;
  --white:#ffffff;
  --ink:#222222;
  --body:#555555;
  --muted:#777777;
  --accent:#2d6a9b;
  --link:#3a8fcc;
  --field:#f1f1f1;
  --field-line:#d6d6d6;
  --footer:#9ecbea;
  --footer-text:#ffffff;
  --bar:#141414;
}
*{box-sizing:border-box;margin:0;padding:0}
html,body{width:978px;height:1200px;overflow:hidden}
body{position:relative;font-family:"Roboto",Arial,sans-serif;background:var(--white);color:var(--ink)}
.hero{position:absolute;left:0;top:0;width:978px;height:548px;background:linear-gradient(170deg,var(--hero) 0%,var(--hero-light) 55%,var(--hero) 100%)}
.topbar{position:absolute;left:0;top:0;width:978px;height:80px;background:rgba(60,120,175,.45)}
.brand{position:absolute;left:72px;top:24px;display:flex;align-items:center;gap:8px;color:var(--white);font-family:"Roboto Condensed",sans-serif;font-weight:700;font-size:25px;letter-spacing:.5px}
.brand-dot{width:26px;height:26px;border-radius:50%;background:var(--white)}
.phone{position:absolute;left:295px;top:32px;display:flex;align-items:center;gap:7px;color:var(--white);font-size:15px;font-weight:300}
.nav{position:absolute;right:72px;top:33px;display:flex;gap:17px;list-style:none}
.nav a{color:var(--white);text-decoration:none;font-size:12px;letter-spacing:.2px}
.headline{position:absolute;left:0;width:978px;text-align:center;color:var(--white);font-weight:400}
.headline.main{top:138px;font-size:19px}
.headline.sub{top:172px;font-size:16px}
.card{position:absolute;top:232px;width:263px;height:316px;background:var(--white);box-shadow:0 0 3px rgba(0,0,0,.15)}
.card-head{height:42px;background:var(--card-head);color:var(--white);font-family:"Roboto Condensed",sans-serif;font-size:17px;text-align:center;line-height:42px}
.card-body{padding:26px 22px 0 20px;font-size:11.5px;line-height:15px;font-weight:300;color:var(--body);text-align:justify}
.card-body p{margin-bottom:8px}
.card-body p.gap{margin-bottom:17px}
.signup{padding:20px 30px 0 26px}
.field{display:block;width:206px;height:32px;margin-bottom:6px;background:var(--field);border:1px solid var(--field-line);border-radius:3px;padding:0 10px;font-family:inherit;font-size:11px;color:#555;line-height:30px}
.field.select{position:relative}
.field.select svg{position:absolute;right:10px;top:12px}
.submit{display:block;width:200px;height:37px;margin-top:8px;border:0;border-radius:3px;background:linear-gradient(#3f7eb1,#225a89);color:var(--white);font-family:inherit;font-size:15px}
.section-title{position:absolute;left:0;top:582px;width:978px;text-align:center;font-size:22px;font-weight:500;color:var(--ink)}
.section-title span{color:var(--accent)}
.product{position:absolute;top:630px;width:206px}
.product-img{width:206px;height:138px;border:3px solid #f0f0f0}
.product h3{margin-top:15px;font-size:12px;font-weight:400;color:var(--ink)}
.product p{margin-top:9px;font-size:9px;line-height:14px;color:var(--muted)}
.product a{display:block;margin-top:8px;font-size:8.5px;color:var(--link);text-decoration:none}
.crowd{position:absolute;left:0;top:886px;width:978px;height:48px;background:linear-gradient(#ffffff,var(--footer))}
.footer{position:absolute;left:0;top:932px;width:978px;height:194px;background:var(--footer);color:var(--footer-text)}
.footer h4{position:absolute;top:38px;font-size:13px;font-weight:400}
.links{position:absolute;left:72px;top:71px;list-style:none;font-size:9px;line-height:20px}
.links li::before{content:"";display:inline-block;border-left:3px solid var(--white);border-top:3px solid transparent;border-bottom:3px solid transparent;margin-right:7px}
.footer .copy{position:absolute;font-size:8.5px;line-height:13.5px;font-weight:300}
.news{position:absolute;left:736px;top:101px;display:flex}
.news-input{width:120px;height:26px;background:#f3f3f3;border:1px solid #dcdcdc;font-size:8px;color:#555;padding:0 10px;line-height:24px}
.news-btn{width:46px;height:26px;background:var(--card-head);color:var(--white);font-size:10px;text-align:center;line-height:26px}
.bar{position:absolute;left:0;top:1126px;width:978px;height:74px;background:var(--bar);color:var(--white)}
.legal{position:absolute;left:74px;top:22px;font-size:10px;line-height:18px}
.social{position:absolute;left:790px;top:22px;display:flex;gap:6px}
.social span{width:24px;height:24px;background:#3b8fd0;border-radius:2px}
.social span:nth-child(2){background:#c4302b}
.social span:nth-child(3){background:#3b5a9a}
.social span:nth-child(4){background:#1d7bb8}
</style>
</head>
<body>
<section class="hero">
  <header class="topbar">
    <div class="brand"><span class="brand-dot"></span>VELMORA</div>
    <div class="phone">
      <svg width="13" height="13" viewBox="0 0 13 13"><rect width="13" height="13" rx="2" fill="#fff"/><path d="M4 3.5c.5 2.8 2.5 5 5.5 5.8l.7-1.3-1.6-.8-.6.7C6.8 7.3 5.8 6.3 5.3 5.1l.7-.6-.8-1.6z" fill="#4f8cbf"/></svg>
      055.7.2,314
    </div>
    <ul class="nav">
      <li><a href="#home">HOME</a></li>
      <li><a href="#products">PRODUCTS</a></li>
      <li><a href="#model">UNIQUE MODEL</a></li>
      <li><a href="#pricing">PRICING</a></li>
      <li><a href="#about">ABOUT</a></li>
      <li><a href="#contact">CONTACT</a></li>
    </ul>
  </header>
  <h1 class="headline main">LIST AND AUDIENCE BUILDING FOR YOUR CONTENT MARKETING EFFORTS</h1>
  <h2 class="headline sub">WE OFFER 2 TRACKS FORM WHICH TO CHOOSE</h2>

  <article class="card" style="left:71px">
    <div class="card-head">TRACK 1</div>
    <div class="card-body">
      <p>Update, enhance or adppend your exist, prospect database We provide contact lists derived from real?</p>
      <p>Coming and technOe Diab nwaeveeo used within your lists Lorem Ipsum has been the industry's standard dummy text ever since the 1500s, when an unknown printer took a galley of type and scrambled it to make a type specimen book.</p>
      <p>It has survived not only five centuries, but also the leap into electronic typesetting, remaining essentially unchanged</p>
    </div>
  </article>

  <article class="card" style="left:362px">
    <div class="card-head">TRACK 2</div>
    <div class="card-body">
      <p class="gap">We use our data and em6lservers to send campaigns for Y. .Vou get access to all the campaign results ba. and only &nbsp;actions</p>
      <p>Lorem Ipsum has been the industry's standard dummy text ever since the 1500s, when an unknown printer took a galley of type and scrambled it to make a type specimen book.</p>
      <p>It has survived not only five centuries, but also the leap into electronic typesetting, remaining essentially unchanged</p>
    </div>
  </article>

  <form class="card" style="left:644px">
    <div class="card-head">TELL US WHAT YOU WANT</div>
    <div class="signup">
      <div class="field">First Name</div>
      <div class="field">Last Name</div>
      <div class="field">Company</div>
      <div class="field">Email</div>
      <div class="field select">Track 1<svg width="10" height="6" viewBox="0 0 10 6"><path d="M0 0h10L5 6z" fill="#222"/></svg></div>
      <button class="submit" type="button">SUBMIT</button>
    </div>
  </form>
</section>

<h2 class="section-title" id="products">OUR <span>PRODUCTS</span></h2>

<article class="product" style="left:72px">
  <div class="product-img" role="img" aria-label="Photo of hands holding a tablet showing charts" style="background:linear-gradient(135deg,#3f8fa8,#d9e4ea 60%,#f2f4f5)"></div>
  <h3>NEQUE PORRO QUISQUAM</h3>
  <p>Lorem Ipsum has been the industry's standard dummy text ever since the 1500s, when</p>
  <a href="#">Read More &gt;&gt;</a>
</article>
<article class="product" style="left:283px">
  <div class="product-img" role="img" aria-label="Photo of a businessman holding a globe with connected devices" style="background:linear-gradient(135deg,#2b4e63,#6f9cb4 50%,#1d2b36)"></div>
  <h3>NEQUE PORRO QUISQUAM</h3>
  <p>Lorem Ipsum has been the industry's standard dummy text ever since the 1500s, when</p>
  <a href="#">Read More &gt;&gt;</a>
</article>
<article class="product" style="left:494px">
  <div class="product-img" role="img" aria-label="Photo of an open hand below a glowing light bulb icon" style="background:radial-gradient(circle at 55% 40%,#f4f4f4,#8a9298 55%,#4a5258)"></div>
  <h3>NEQUE PORRO QUISQUAM</h3>
  <p>Lorem Ipsum has been the industry's standard dummy text ever since the 1500s, when</p>
  <a href="#">Read More &gt;&gt;</a>
</article>
<article class="product" style="left:705px">
  <div class="product-img" role="img" aria-label="Photo of a smartphone over a blue network world map" style="background:linear-gradient(135deg,#1f6fb0,#5aaee3 50%,#1a5e9a)"></div>
  <h3>NEQUE PORRO QUISQUAM</h3>
  <p>Lorem Ipsum has been the industry's standard dummy text ever since the 1500s, when</p>
  <a href="#">Read More &gt;&gt;</a>
</article>

<div class="crowd" role="img" aria-label="Row of light blue head silhouettes forming the top edge of the footer"></div>

<footer class="footer" id="contact">
  <h4 style="left:72px">LINKS</h4>
  <ul class="links">
    <li>Home</li><li>About us</li><li>Property</li><li>L ocation</li><li>Contacts</li>
  </ul>
  <h4 style="left:228px;top:36px">NEQUE PORRO QUISQUAM</h4>
  <p class="copy" style="left:226px;top:70px;width:188px">&nbsp;Lorem Ipsum has been the industry's standard dummy text ever since the 1500s, when an unknown printer took<br><span style="display:block;margin-top:6px">a galley of type and scrambled it to make a type specimen book. It has survived not only five centuries, but also the leap into electronic typeset-</span></p>
  <h4 style="left:527px">GET IN TOUCH</h4>
  <p class="copy" style="left:528px;top:72px;font-size:9px;line-height:18px">Address : 1240 Harbor Lane,<br>Cedar Point, OR<br><span style="display:block;margin-top:9px">Phone : 503 618 2207</span><span style="display:block;margin-top:9px">Email : hello@velmoramail.com</span></p>
  <h4 style="left:736px">NEWSLETTER</h4>
  <p class="copy" style="left:736px;top:72px;width:160px;font-size:9px">Your about us information would fit here nicely.</p>
  <div class="news"><div class="news-input">Email address</div><div class="news-btn">Submit</div></div>
</footer>

<div class="bar">
  <p class="legal">Privacy Policy &nbsp;| &nbsp;Terms of Use &nbsp;| &nbsp;About Us &nbsp;| &nbsp;Sitemap<br>Copyright © 2016 &nbsp;All Rights</p>
  <div class="social"><span></span><span></span><span></span><span></span></div>
</div>
</body>
</html>
```